Business card design needed

see my website

www.aldermoorandpike.com

I am after a new logo and business card needs to fit in with the website. I like the look of typewriter text - would like this on the website as well if I could!

Industry/Entity Type

Business

Contact Information for Business Card

Aldermoor and Pike
Design and Heritage Consultants

Marisa Oakton
Principal

+61 407 963 215
marisa@aldermoorandpike.com

www.aldermoorandpike.com

back of card

Interior Design
Consultancy on Period Home restoration and renovation
Heritage Impact Statements
Conservation Management Plans
Materials Conservation
Historical Research

```html
<!DOCTYPE html>
<html lang="en">
<head>
<meta charset="utf-8">
<title>Aldermoor and Pike — Business Card</title>
<link rel="stylesheet" href="https://fonts.googleapis.com/css2?family=Courier+Prime:wght@400;700&family=Special+Elite&display=swap">
<style>
  :root {
    --paper: #f6f2e2;
    --paper-shade: #ece6cf;
    --mint: #4fe89c;
    --slate: #475152;
    --ink: #2b2b2b;
  }
  html, body {
    margin: 0;
    padding: 0;
    width: 1200px;
    height: 695px;
    overflow: hidden;
    background: var(--paper);
  }
  .card {
    position: relative;
    width: 1200px;
    height: 695px;
    background: radial-gradient(ellipse at 30% 40%, var(--paper) 0%, var(--paper) 55%, var(--paper-shade) 100%);
    overflow: hidden;
  }
  .brand {
    position: absolute;
    left: 79px;
    top: 128px;
    width: 620px;
  }
  .brand-name {
    margin: 0;
    font-family: "Special Elite", "Courier New", monospace;
    font-weight: 400;
    font-size: 55px;
    line-height: 1;
    color: var(--mint);
    white-space: nowrap;
  }
  .brand-tagline {
    margin: 22px 0 0;
    font-family: "Special Elite", "Courier New", monospace;
    font-size: 33px;
    line-height: 1;
    color: var(--slate);
    white-space: nowrap;
    letter-spacing: 0.5px;
  }
  .person {
    position: absolute;
    right: 68px;
    top: 346px;
    text-align: right;
  }
  .person-name {
    margin: 0;
    font-family: "Special Elite", "Courier New", monospace;
    font-size: 37px;
    line-height: 1;
    color: var(--mint);
  }
  .person-role {
    margin: 22px 0 0;
    font-family: "Courier Prime", "Courier New", monospace;
    font-size: 31px;
    line-height: 1;
    color: var(--ink);
  }
  .contacts {
    position: absolute;
    left: 85px;
    top: 503px;
    margin: 0;
    padding: 0;
    list-style: none;
  }
  .contact {
    display: flex;
    align-items: center;
    height: 34px;
    margin-bottom: 7px;
    font-family: "Courier Prime", "Courier New", monospace;
    font-size: 28px;
    color: var(--ink);
    letter-spacing: 1px;
  }
  .contact-web { font-weight: 700; }
  .contact-icon {
    width: 32px;
    height: 32px;
    margin-right: 16px;
    flex: none;
  }
</style>
</head>
<body>
<main class="card">
  <header class="brand">
    <h1 class="brand-name">Aldermoor and Pike</h1>
    <p class="brand-tagline">Heritage &amp; Design Consultants</p>
  </header>

  <section class="person">
    <p class="person-name">Marisa Oakton</p>
    <p class="person-role">Principal</p>
  </section>

  <ul class="contacts">
    <li class="contact contact-phone">
      <svg class="contact-icon" viewBox="0 0 32 32" aria-hidden="true">
        <circle cx="16" cy="16" r="14" fill="none" stroke="var(--mint)" stroke-width="2"/>
        <path d="M11.5 9.5c1-.8 2-.6 2.5.3l1 2c.3.7.1 1.3-.5 1.8l-.8.6c.7 1.8 2 3.2 3.8 4l.6-.8c.5-.6 1.2-.8 1.9-.4l2 1.1c.8.5 1 1.5.2 2.4-1.5 1.7-3.5 1.6-6 .1-2.8-1.8-4.7-4.5-5.4-7.3-.3-1.6 0-2.9.7-3.8z" fill="var(--mint)"/>
      </svg>
      <span>+61 407 963 215</span>
    </li>
    <li class="contact contact-email">
      <svg class="contact-icon" viewBox="0 0 32 32" aria-hidden="true">
        <circle cx="16" cy="16" r="14" fill="none" stroke="var(--mint)" stroke-width="2"/>
        <path d="M9 14l7-5 7 5v8H9z" fill="var(--mint)"/>
        <path d="M9.5 14.5l6.5 4.5 6.5-4.5" fill="none" stroke="var(--paper)" stroke-width="1.4"/>
      </svg>
      <span>marisa@aldermoorandpike.com</span>
    </li>
    <li class="contact contact-web">
      <svg class="contact-icon" viewBox="0 0 32 32" aria-hidden="true">
        <circle cx="16" cy="16" r="14" fill="none" stroke="var(--mint)" stroke-width="2"/>
        <circle cx="16" cy="16" r="7" fill="var(--mint)"/>
        <path d="M9 16h14M16 9v14M12.5 10.5c-2 3.5-2 7.5 0 11M19.5 10.5c2 3.5 2 7.5 0 11" fill="none" stroke="var(--paper)" stroke-width="1.1"/>
      </svg>
      <span>www.aldermoorandpike.com</span>
    </li>
  </ul>
</main>
</body>
</html>
```